K&T Holdings

Design a modern simple business card. I have attached a clean version of a card we like form Marrowfield Partners another company we own. I also attached the old K&T card design and logo and a couple of ideas we had but just can't finalize on whether we like them or not. We would like to include the 20 year logo somewhere on the card.

```html
<!DOCTYPE html>
<html lang="en">
<head>
<meta charset="utf-8">
<title>K&amp;T Holdings — Business Card</title>
<link rel="stylesheet" href="https://fonts.googleapis.com/css2?family=DM+Sans:wght@400;500;700&display=swap">
<style>
  :root {
    --navy: #272560;
    --grey: #8a8a8c;
    --paper: #ffffff;
    --backdrop: #eeefef;
    --rule: #272560;
  }
  * { box-sizing: border-box; margin: 0; padding: 0; }
  html, body {
    width: 910px; height: 1200px; overflow: hidden;
    background: var(--backdrop);
    font-family: "DM Sans", sans-serif;
  }
  .sheet {
    width: 910px; height: 1200px;
    display: flex; flex-direction: column; align-items: center; justify-content: center;
    gap: 90px;
  }
  .card {
    position: relative;
    width: 700px; height: 400px;
    background: var(--paper);
    box-shadow: 0 2px 8px rgba(0,0,0,0.18);
    overflow: hidden;
  }

  /* Front */
  .card-front .brand-row {
    position: absolute; left: 0; right: 0; top: 95px; height: 190px;
    display: flex; align-items: center; justify-content: center;
  }
  .wordmark {
    display: flex; align-items: center; gap: 14px;
    color: var(--navy); font-weight: 700; font-size: 78px; letter-spacing: -1px;
  }
  .wordmark .dot {
    width: 22px; height: 22px; border-radius: 50%; background: var(--grey);
  }
  .divider {
    width: 2px; height: 190px; background: var(--rule); margin: 0 42px;
  }
  .anniversary {
    display: flex; flex-direction: column; align-items: flex-start;
    color: var(--navy); font-weight: 500;
  }
  .anniversary .years { font-size: 68px; line-height: 1; }
  .anniversary .span { font-size: 30px; letter-spacing: 1.5px; margin-top: 6px; }
  .address-band {
    position: absolute; left: 0; right: 0; bottom: 26px; height: 28px;
    background: var(--navy); color: #fff;
    display: flex; align-items: center; justify-content: center;
    font-size: 17px; letter-spacing: 1.6px; font-weight: 500;
  }

  /* Back */
  .contact-panel {
    position: absolute; left: 0; top: 12px; bottom: 22px; width: 375px;
    background: var(--navy); color: #fff;
    padding: 72px 0 0 36px;
  }
  .person-name { font-size: 34px; font-weight: 700; letter-spacing: 0.3px; line-height: 1; }
  .person-title { font-size: 20px; font-weight: 400; margin-top: 6px; }
  .contact-list { list-style: none; margin-top: 34px; }
  .contact-list li {
    display: flex; align-items: center; gap: 14px;
    font-size: 18px; height: 45px;
  }
  .contact-list svg { width: 26px; height: 26px; flex: none; }
  .card-back .wordmark {
    position: absolute; left: 375px; right: 0; top: 0; bottom: 0;
    justify-content: center;
  }
</style>
</head>
<body>
<main class="sheet">

  <section class="card card-front" aria-label="Card front">
    <div class="brand-row">
      <div class="wordmark"><span class="dot"></span>K&amp;T</div>
      <div class="divider"></div>
      <div class="anniversary">
        <span class="years">20 YEARS</span>
        <span class="span">2004-2024</span>
      </div>
    </div>
    <div class="address-band">218 Cedar Avenue, Suite 400, Lakemont, TX 77590</div>
  </section>

  <section class="card card-back" aria-label="Card back">
    <div class="contact-panel">
      <h1 class="person-name">DEREK HOLLOWAY</h1>
      <p class="person-title">IT Director</p>
      <ul class="contact-list">
        <li>
          <svg viewBox="0 0 26 26" aria-hidden="true">
            <circle cx="13" cy="13" r="13" fill="#fff"/>
            <rect x="7" y="8.5" width="12" height="9" rx="1" fill="#272560"/>
            <path d="M7.5 9.2 L13 13.5 L18.5 9.2" stroke="#fff" stroke-width="1.2" fill="none"/>
          </svg>
          dholloway@ktholdltd.com
        </li>
        <li>
          <svg viewBox="0 0 26 26" aria-hidden="true">
            <circle cx="13" cy="13" r="13" fill="#fff"/>
            <path d="M9 7 L11.5 7 L12.5 10 L11 11.3 C11.8 13 13 14.2 14.7 15 L16 13.5 L19 14.5 L19 17 C19 18 18 19 17 19 C12 18.5 7.5 14 7 9 C7 8 8 7 9 7 Z" fill="#272560"/>
          </svg>
          409-555-0142
        </li>
        <li>
          <svg viewBox="0 0 26 26" aria-hidden="true">
            <circle cx="13" cy="13" r="13" fill="#fff"/>
            <rect x="9" y="6" width="8" height="14" rx="1.5" fill="#272560"/>
            <rect x="10.3" y="7.8" width="5.4" height="9" fill="#fff"/>
            <circle cx="13" cy="18.3" r="0.8" fill="#fff"/>
          </svg>
          409-555-0187
        </li>
      </ul>
    </div>
    <div class="wordmark"><span class="dot"></span>K&amp;T</div>
  </section>

</main>
</body>
</html>
```